Packaging design coffee brand

Creating a packaging design for coffee products. an existing brand shall be repositioned, complete redesign. capsules, beans, etc. We need a label for the coffee whole bean package, a folded packaging for coffee capsules, see attachment. The package for the whole bean also shall be changed into a full printed packaging.

The logo is already created, but you can play with the elements, the position of symbol and name.

Target Market(s)

Europe

Industry/Entity Type

coffee

Font styles to use
Sans Serif

Requirements
Must have
• we already have a logo, which shall be used. Position of the symbol and name can be adjusted.
Nice to have
• please see the briefing attached, there you find al relevant information.
Should not have
• shall not be ecological, it shal be a lifestyle brand.

```html
<!DOCTYPE html>
<html lang="en">
<head>
<meta charset="utf-8">
<title>Velma Roast – Whole Bean Coffee Pouch</title>
<link rel="stylesheet" href="https://fonts.googleapis.com/css2?family=Josefin+Sans:wght@400&family=Poppins:wght@600&family=Ubuntu:wght@400&family=Roboto:wght@400;700;900&display=swap">
<style>
  :root {
    --page: #f3f4f4;
    --teal: #3cbfa4;
    --teal-light: #4fd0b5;
    --teal-deep: #23967f;
    --ink: #3a3b3d;
  }
  * { box-sizing: border-box; margin: 0; padding: 0; }
  html, body { width: 1200px; height: 1098px; overflow: hidden; background: var(--page); }
  .stage { position: relative; width: 1200px; height: 1098px; }

  .pouch {
    position: absolute; top: 150px; width: 520px; height: 800px;
    background: linear-gradient(160deg, var(--teal-light) 0%, var(--teal) 45%, var(--teal-deep) 100%);
    overflow: hidden; color: var(--ink);
  }
  .pouch--front { left: 50px; }
  .pouch--back { left: 630px; }

  .pouch__zip {
    position: absolute; left: 0; right: 0; top: 70px; height: 14px;
    border-top: 2px solid rgba(255,255,255,.25); border-bottom: 2px solid rgba(0,0,0,.12);
  }

  .brand {
    position: absolute; left: 0; right: 0; text-align: center;
    font-family: "Josefin Sans", sans-serif; font-weight: 400;
    letter-spacing: 3px; color: var(--ink);
    display: flex; align-items: center; justify-content: center; gap: 14px;
  }
  .brand__dot { width: 22px; height: 22px; border-radius: 50%; background: var(--ink); }
  .pouch--front .brand { top: 250px; font-size: 44px; }
  .pouch--back .brand { top: 215px; font-size: 40px; }

  .product-name {
    position: absolute; top: 360px; left: 0; right: 0; text-align: center;
    font-family: "Poppins", sans-serif; font-weight: 600; font-size: 34px; line-height: 1.1;
    color: var(--ink);
  }

  .front-artwork {
    position: absolute; left: 0; right: 0; top: 470px; bottom: 0;
    background: linear-gradient(to bottom, rgba(58,59,61,0) 0%, rgba(58,59,61,.75) 40%, var(--ink) 70%);
  }

  .claims {
    position: absolute; left: 0; right: 0; bottom: 40px; text-align: center;
    font-family: "Ubuntu", sans-serif; font-size: 17px; color: var(--teal);
  }
  .claims__rule { width: 170px; height: 2px; background: var(--teal); margin: 8px auto 10px; }

  .back-copy {
    position: absolute; left: 40px; top: 320px; width: 230px;
    font-family: "Roboto", sans-serif; font-size: 15px; line-height: 1.3;
    text-align: justify; color: var(--ink);
  }
  .back-copy p + p { margin-top: 24px; text-align: left; }
  .net-weight { margin-top: 22px; font-size: 16px; }

  .nutrition {
    position: absolute; left: 290px; top: 325px; width: 190px;
    border: 1px solid var(--ink); padding: 4px 5px;
    font-family: "Roboto", sans-serif; color: var(--ink); font-size: 7px;
  }
  .nutrition__title { font-weight: 900; font-size: 20px; line-height: 1; }
  .nutrition__serving { display: flex; justify-content: space-between; font-weight: 700; font-size: 9px; border-bottom: 5px solid var(--ink); padding-bottom: 2px; }
  .nutrition__cal { display: flex; justify-content: space-between; align-items: flex-end; font-weight: 900; font-size: 16px; border-bottom: 3px solid var(--ink); }
  .nutrition__cal small { display: block; font-size: 6px; font-weight: 700; }
  .nutrition__dv { text-align: right; font-weight: 700; font-size: 6px; border-bottom: 1px solid var(--ink); }
  .nutrition__row { display: flex; justify-content: space-between; border-bottom: 1px solid var(--ink); padding: 1px 0; }
  .nutrition__row--sub { padding-left: 10px; }
  .nutrition__row--sub2 { padding-left: 18px; }
  .nutrition b { font-weight: 700; }

  .code-box {
    position: absolute; left: 312px; top: 600px; width: 135px; height: 72px;
    background: var(--ink);
  }
</style>
</head>
<body>
<main class="stage">

  <section class="pouch pouch--front">
    <div class="pouch__zip"></div>
    <div class="front-artwork" role="img" aria-label="Decorative dark wave with a light line and leaf rising across the lower pouch"></div>
    <div class="brand"><span class="brand__dot"></span>VELMA ROAST</div>
    <h1 class="product-name">WHOLE<br>BEAN COFFEE</h1>
    <div class="claims">
      <div>100% Arabica Blend.</div>
      <div class="claims__rule"></div>
      <div>Organic and Fair Trade Certified</div>
    </div>
  </section>

  <section class="pouch pouch--back">
    <div class="pouch__zip"></div>
    <div class="brand"><span class="brand__dot"></span>VELMA ROAST</div>
    <div class="back-copy">
      <p>Lorem ipsum dolor sit amet, consectetuer adipiscing elit, sed diam nonummy nibh euismod tincidunt ut laoreet dolore magna aliquam erat volutpat. Ut wisi enim ad minim veniam, quis nostrud exerci tation ullamcorper suscipit lobortis nisl ut aliquip ex ea commodo consequat. Duis autem vel eum iriure dolor in hendrerit. Lorem ipsum dolor sit amet, consectetuer ullamcorper suscipit lobortis nisl ut aliquip ex ea commodo consequat. Duis autem vel eum iriure dolor in hendrerit.</p>
      <p>Lorem ipsum dolor sit amet, consectetuer adipiscing elit, sed diam nonummy nibh euismod</p>
      <p class="net-weight">NET WT 12 OZ (340g)</p>
    </div>
    <div class="nutrition">
      <div class="nutrition__title">Nutrition Facts</div>
      <div>10 servings per container</div>
      <div class="nutrition__serving"><span>Serving size</span><span>1 cup (55g)</span></div>
      <div class="nutrition__cal"><span><small>Amount per serving</small>Calories</span><span>165</span></div>
      <div class="nutrition__dv">% Daily Value*</div>
      <div class="nutrition__row"><span><b>Total Fat</b> 1.5g</span><b>2%</b></div>
      <div class="nutrition__row nutrition__row--sub"><span>Saturated Fat 0.5g</span><b>3%</b></div>
      <div class="nutrition__row nutrition__row--sub"><span>Trans Fat 0g</span><span></span></div>
      <div class="nutrition__row nutrition__row--sub"><span>Polyunsaturated Fat 0.5g</span><span></span></div>
      <div class="nutrition__row nutrition__row--sub"><span>Monounsaturated Fat 0.5g</span><span></span></div>
      <div class="nutrition__row"><span><b>Cholesterol</b> 0mg</span><b>0%</b></div>
      <div class="nutrition__row"><span><b>Sodium</b> 180mg</span><b>8%</b></div>
      <div class="nutrition__row"><span><b>Fluoride</b> 0g</span><span></span></div>
      <div class="nutrition__row"><span><b>Total Carbohydrate</b> 21g</span><b>8%</b></div>
      <div class="nutrition__row nutrition__row--sub"><span>Dietary Fiber 2g</span><b>7%</b></div>
      <div class="nutrition__row nutrition__row--sub2"><span>Soluble Fiber &lt;1g</span><span></span></div>
      <div class="nutrition__row nutrition__row--sub2"><span>Insoluble Fiber 1g</span><span></span></div>
      <div class="nutrition__row nutrition__row--sub"><span>Total Sugars 8g</span><span></span></div>
      <div class="nutrition__row nutrition__row--sub2"><span>Includes 6g Added Sugars</span><b>12%</b></div>
    </div>
    <div class="code-box"></div>
  </section>

</main>
</body>
</html>
```